Brightmoor Law Letterhead for Law firm must be modern and use the logo I uploaded.

Hello I want a clean modern professional letterhead for my law firm Brightmoor Law. A logo has already been created and all files have been uploaded. The information for the firm can be given through message. Please use the logo that has already been created. Please also use the color scheme of that logo. (blue and white).

Target Market(s)

General Public

Industry/Entity Type

Law Firm

Colors

Designer to choose colors to be used in the design.

Requirements
Must have
• This must be a modern professional letterhead
Nice to have
• My logo that is included in file form
Should not have
• Should not have logo that is not the one I uploaded.

```html
<!DOCTYPE html>
<html lang="en">
<head>
<meta charset="utf-8">
<title>Brightmoor Law Letterhead</title>
<link href="https://fonts.googleapis.com/css2?family=Roboto:wght@400;500&display=swap" rel="stylesheet">
<style>
  :root {
    --navy: #2b3262;
    --rule: #6d6f9a;
    --paper: #ffffff;
    --ink-soft: #4a4a55;
    --backdrop: #d9d9dc;
  }
  * { margin: 0; padding: 0; box-sizing: border-box; }
  html, body { width: 1200px; height: 800px; overflow: hidden; }
  body {
    background: var(--backdrop);
    font-family: "Roboto", Arial, sans-serif;
    position: relative;
  }
  .sheet {
    position: absolute;
    top: 50px;
    width: 495px;
    height: 700px;
    box-shadow: 0 6px 24px rgba(0,0,0,0.18);
  }
  .sheet--front { left: 90px; background: var(--paper); }
  .sheet--back { left: 625px; background: var(--navy); }

  .letterhead-header {
    position: absolute;
    top: 70px;
    left: 0;
    width: 100%;
    text-align: center;
  }
  .firm-name {
    color: var(--navy);
    font-size: 15px;
    font-weight: 400;
    letter-spacing: 0.42em;
    text-transform: uppercase;
    padding-left: 0.42em;
  }

  .letterhead-footer {
    position: absolute;
    left: 50px;
    right: 50px;
    bottom: 44px;
    text-align: center;
    color: var(--ink-soft);
    font-size: 8.5px;
  }
  .footer-rule {
    height: 1px;
    background: var(--rule);
    margin-bottom: 14px;
  }
  .footer-address { margin-bottom: 5px; }
  .footer-contacts {
    display: flex;
    justify-content: center;
    gap: 14px;
  }
  .contact-item {
    display: inline-flex;
    align-items: center;
    gap: 4px;
  }
  .contact-icon { width: 8px; height: 8px; fill: var(--navy); }
</style>
</head>
<body>
  <section class="sheet sheet--front" aria-label="Letterhead front">
    <header class="letterhead-header">
      <div class="firm-name">Brightmoor Law</div>
    </header>

    <footer class="letterhead-footer">
      <div class="footer-rule"></div>
      <p class="footer-address">4820 West Harlow Street Suite 12 Maple Ridge, CO 80214</p>
      <p class="footer-contacts">
        <span class="contact-item">
          <svg class="contact-icon" viewBox="0 0 10 10" aria-hidden="true"><path d="M2.2 0.5l1.6 2-1 1.1c.6 1.3 1.5 2.2 2.8 2.8l1.1-1 2 1.6-.9 1.9C4.2 8.7 1.3 5.8.3 1.4z"/></svg>
          555.014.2290
        </span>
        <span class="contact-item">
          <svg class="contact-icon" viewBox="0 0 10 10" aria-hidden="true"><path d="M0 2h10v6H0z M0.6 2.4L5 5.6 9.4 2.4" stroke="#fff" stroke-width="0.8"/></svg>
          info@brightmoorlaw.com
        </span>
        <span class="contact-item">
          <svg class="contact-icon" viewBox="0 0 10 10" aria-hidden="true"><circle cx="5" cy="5" r="4.6"/><path d="M0.5 5h9M5 0.5c-2.2 2.6-2.2 6.4 0 9M5 0.5c2.2 2.6 2.2 6.4 0 9" stroke="#fff" stroke-width="0.6" fill="none"/></svg>
          www.brightmoorlaw.com
        </span>
      </p>
    </footer>
  </section>

  <section class="sheet sheet--back" aria-label="Letterhead reverse side, solid navy"></section>
</body>
</html>
```